Business Card/ Email Signature Design Project

I am an Interior Designer. I need a business card that looks sophisticated stylish but simple in design. My work covers space design/ interior architecture/ furniture design/ product development & styling.

I have a very specific brief and know mostly what I want. I'm hoping to work with someone who can translate my ideas.

My branding should have a strong focus on my name, the majority of my work is referral based.
I'm keen to keep a monochromatic colour scheme: dark charcoal/ black/ white/ embossing/ silver. I'm not suggesting we use all that I've listed, they are possible ideas at this stage. I will need to be mindful of printing costs an also how I make the design work across, cards, letter heads, email logo and web design.

Theory behind images sent below;
1-Rug Image_(minus boarder) I was thinking this image could be used on the back of the card with my contact details over. I like that the lines are almost hand drawn and start to look free form. It's a subtle contrast to a more formal front of the card with my name.
2_Owen Ratley_I really like the orientation, the proportion of font on the card, the colour and the font. I like the lower case for my name and the upper case for 'Interior Design'. Not sure if it should be 'Interior Designer or Interior Design' at this stage, was leaning towards 'Interior Design'. Was thinking the 'i' and 'd' in my surname could be the colour eg 'silver'?? We can decide on this once we see it.

Look forward to hearing from you.
Cheers,
Noreen Bastoli

Industry/Entity Type

Printing

Logo Text

Noreen Bastoli Interior Design

```html
<!DOCTYPE html>
<html lang="en">
<head>
<meta charset="utf-8">
<title>Noreen Bastoli Interior Design – Business Card Concepts</title>
<link rel="stylesheet" href="https://fonts.googleapis.com/css2?family=Source+Sans+3:wght@400;600;700&display=swap">
<style>
  :root {
    --canvas: #ffffff;
    --charcoal: #54514e;
    --ink: #111111;
    --cream: #ece6d8;
    --rug-light: #ecebe6;
    --rug-mid: #d9d8d2;
    --rug-blush: #eadfdc;
    --rug-blush-mid: #e3d3d2;
  }
  * { margin: 0; padding: 0; box-sizing: border-box; }
  html, body { width: 966px; height: 1200px; overflow: hidden; background: var(--canvas); }
  body { position: relative; font-family: "Source Sans 3", "Myriad Pro", sans-serif; color: var(--ink); }

  .card {
    position: absolute;
    width: 444px;
    height: 254px;
    display: flex;
    flex-direction: column;
    align-items: center;
    justify-content: center;
  }
  .col-left { left: 0; }
  .col-right { left: 514px; }
  .row-1 { top: 0; }
  .row-2 { top: 296px; }
  .row-3 { top: 592px; }
  .row-4 { top: 902px; }

  .card--front { background: var(--charcoal); }

  .wordmark {
    font-weight: 600;
    font-size: 44px;
    line-height: 1;
    letter-spacing: -0.5px;
    color: var(--ink);
  }
  .tagline {
    font-weight: 400;
    font-size: 24px;
    line-height: 1;
    letter-spacing: 4.4px;
    margin-top: 2px;
    color: var(--ink);
  }
  .tagline--bold { font-weight: 600; }
  .card--light-name .wordmark { color: var(--cream); }

  .card--back { overflow: hidden; }
  .rug-texture {
    position: absolute;
    inset: 0;
    width: 100%;
    height: 100%;
  }
  .rug-texture--grey { background: radial-gradient(ellipse at 40% 50%, var(--rug-light), var(--rug-mid)); }
  .rug-texture--blush { background: radial-gradient(ellipse at 40% 50%, var(--rug-light), var(--rug-blush-mid)); }

  .contact {
    position: relative;
    text-align: center;
    font-weight: 700;
    margin-left: -8px;
  }
  .contact__address { font-size: 22px; line-height: 1.3; }
  .contact__lines { margin-top: 14px; font-size: 17px; line-height: 1.35; }
</style>
</head>
<body>

  <section class="card card--front col-left row-1">
    <p class="wordmark">noreen bastoli</p>
    <p class="tagline">INTERIOR DESIGN</p>
  </section>

  <section class="card card--front col-right row-1">
    <p class="wordmark">noreen bastoli</p>
    <p class="tagline tagline--bold">INTERIOR DESIGN</p>
  </section>

  <section class="card card--front col-left row-2">
    <p class="wordmark">noreen bastoli</p>
    <p class="tagline">INTERIOR DESIGN</p>
  </section>

  <section class="card card--front col-right row-2">
    <p class="wordmark">noreen bastoli</p>
    <p class="tagline tagline--bold">INTERIOR DESIGN</p>
  </section>

  <section class="card card--back col-left row-3">
    <div class="rug-texture rug-texture--grey" role="img" aria-label="Rug texture with free-form grey hand-drawn line pattern"></div>
    <address class="contact">
      <p class="contact__address">48 Alder Lane<br>Glendale Heights Illinois<br>60139</p>
      <p class="contact__lines">T: 555-318-2046<br>noreen@bastolistudio.com<br>www.bastolistudio.com</p>
    </address>
  </section>

  <section class="card card--front card--light-name col-right row-3">
    <p class="wordmark">noreen bastoli</p>
    <p class="tagline tagline--bold">INTERIOR DESIGN</p>
  </section>

  <section class="card card--back col-left row-4">
    <div class="rug-texture rug-texture--blush" role="img" aria-label="Rug texture with free-form pink hand-drawn line pattern"></div>
    <address class="contact">
      <p class="contact__address">48 Alder Lane<br>Glendale Heights Illinois<br>60139</p>
      <p class="contact__lines">T: 555-318-2046<br>noreen@bastolistudio.com<br>www.bastolistudio.com</p>
    </address>
  </section>

  <section class="card card--front card--light-name col-right row-4">
    <p class="wordmark">noreen bastoli</p>
    <p class="tagline tagline--bold">INTERIOR DESIGN</p>
  </section>

</body>
</html>
```